Blue Heron Concrete Coating - Builders Flyer

The goal of this flyer is to sell our services to home builders to include our services as an upgrade for new home purchases.
Flyer should be two sided full color.
Colors, font, look/feel should match company website.
Our company is "Blue Heron Concrete Coating".
We specialize in decorative concrete coatings; including Concrete staining and sealing, Epoxy flake and quartz, Polished Concrete, Concrete resurfacing & overlay, Concrete crack repairs, Pool deck spray texture and Stamped concrete.
Applications include: Garages, Patios, Pool decks, Driveways, Basements, Counter & Bar tops.
See attached files for company logo, contact info and project photos.

```html
<!DOCTYPE html>
<html lang="en">
<head>
<meta charset="utf-8">
<title>Blue Heron Concrete Coating – Builders Flyer</title>
<link href="https://fonts.googleapis.com/css2?family=Poppins:wght@300;400;500;600;700;800&display=swap" rel="stylesheet">
<style>
:root{
  --navy:#1f2b3e;
  --navy-2:#2c3a52;
  --yellow:#f6c81b;
  --olive:#8d8a3c;
  --ink:#1c2433;
  --grey-box:#ececec;
  --bg:#d6d6d6;
  --white:#ffffff;
  --link-blue:#2e6ad1;
}
*{margin:0;padding:0;box-sizing:border-box}
html,body{width:1200px;height:968px;overflow:hidden;background:var(--bg);font-family:'Poppins',sans-serif;color:var(--ink)}
.page{position:absolute;top:156px;width:508px;height:656px;background:var(--white);overflow:hidden}
.page--front{left:74px}
.page--back{left:618px}
.abs{position:absolute}
.photo{position:absolute}

/* front */
.side-band{left:379px;top:0;width:129px;height:656px;background:linear-gradient(180deg,#24324a,#1c2638)}
.side-band__word{left:52px;top:40px;writing-mode:vertical-rl;font-weight:800;font-size:96px;color:rgba(255,255,255,.025);letter-spacing:2px;white-space:nowrap}
.brand{left:32px;top:30px;display:flex;align-items:center;gap:8px}
.brand__mark{width:34px;height:24px;background:#c9a58c}
.brand__name{font-weight:700;font-size:19px;line-height:1;color:var(--ink)}
.brand__tag{font-size:6.5px;letter-spacing:2.6px;font-weight:500;margin-top:3px}
.bracket{left:32px;top:92px;width:14px;height:302px;border-left:1.5px solid var(--ink);border-top:1.5px solid var(--ink);border-bottom:1.5px solid var(--ink)}
.headline{left:52px;top:80px;line-height:1}
.headline__a{font-size:18px;font-weight:400}
.headline__b{font-size:29px;font-weight:800;margin-top:2px}
.headline__c{font-size:17.5px;font-weight:700;margin-top:2px}
.frame{left:226px;top:92px;width:249px;height:302px;border:1px solid #d8dde6}
.badge{left:182px;top:228px;width:88px;height:88px;border-radius:50%;background:var(--navy);border:2.5px solid var(--yellow);display:flex;flex-direction:column;align-items:center;justify-content:center;text-align:center;line-height:1.15}
.badge__top{color:var(--yellow);font-weight:700;font-size:8.5px}
.badge__bot{color:#fff;font-size:8.5px;font-weight:400}
.spec-title{left:52px;top:388px;font-size:13.5px;font-weight:400}
.spec-title b{font-weight:700}
.spec-sub{left:52px;top:409px;font-size:8.5px;font-weight:600}
.list{list-style:none;font-size:7.6px;line-height:11.6px}
.list li{position:relative;padding-left:10px}
.list li::before{content:"";position:absolute;left:0;top:3.5px;width:5px;height:5px;border-radius:50%;background:var(--yellow)}
.spec-col1{left:52px;top:429px}
.spec-col2{left:199px;top:429px;border-left:1px solid #c8c8c8;padding-left:9px}
.about{left:54px;top:488px;width:312px;height:56px;background:var(--grey-box);padding:10px 11px;font-size:7.3px;line-height:9px}
.about b{font-weight:600}

/* footer */
.owner-photo{left:51px;top:562px;width:62px;height:62px;border-radius:50%;background:radial-gradient(circle at 50% 40%,#7a6a58,#2b2a2b);border:2px solid var(--navy)}
.owner-name{left:116px;top:582px;width:94px;height:18px;background:var(--navy);border-radius:0 9px 9px 0;color:#fff;font-size:11.5px;font-weight:500;padding-left:10px;line-height:18px;white-space:nowrap}
.owner-name b{font-weight:700}
.owner-name span{color:var(--yellow)}
.owner-role{left:126px;top:603px;font-size:7.5px;font-weight:600}
.contacts{left:230px;top:581px;font-size:7.8px;font-weight:600;line-height:13px}
.contacts div{display:flex;align-items:center;gap:5px}
.contacts svg{width:9px;height:9px;flex:none}
.free{top:580px;width:80px;height:42px;border:1px dashed #9aa;display:flex;flex-direction:column;align-items:center;justify-content:center;line-height:1}
.free__big{font-size:24px;font-weight:800;color:var(--yellow)}
.free__small{font-size:8px;font-weight:700;letter-spacing:1px;margin-top:1px}
.free--dark .free__small{color:#fff}
.free--front{left:395px}
.free--back{left:395px}

/* back */
.top-band{left:0;top:0;width:508px;height:194px;background:linear-gradient(90deg,#1f2b3e,#2d3c55 60%,#1f2b3e)}
.svc-frame{left:31px;top:38px;width:12px;height:110px;border-left:1px solid #8b95a6;border-top:1px solid #8b95a6}
.svc-title{left:51px;top:30px;color:#fff;font-size:13px;font-weight:400}
.svc-title b{color:var(--yellow);font-weight:700}
.list--light{color:#fff;font-size:7px;line-height:10.9px}
.svc-list{left:51px;top:53px}
.app-pill{left:199px;top:32px;width:26px;height:116px;background:linear-gradient(180deg,#3a4660,var(--olive));border-radius:0 0 13px 13px;display:flex;align-items:center;justify-content:center}
.app-pill span{writing-mode:vertical-rl;transform:rotate(180deg);color:#fff;font-weight:700;font-size:12px;letter-spacing:1px}
.app-frame{left:226px;top:34px;width:249px;height:112px;border:1px solid #6f7a8c;border-left:none}
.app{display:flex;align-items:center;gap:7px;color:#fff;font-size:7.8px;font-weight:500}
.icon{width:22px;height:22px;border-radius:50%;background:var(--yellow);border:2px solid #e8d47a;display:flex;align-items:center;justify-content:center;flex:none}
.icon svg{width:11px;height:11px}
.shot{top:158px;width:108px;height:70px}
.cap{top:228px;width:108px;height:14px;background:var(--navy);color:#fff;font-size:6.8px;font-weight:600;text-align:center;line-height:14px}
.h-side{font-size:13px;font-weight:700}
.h-side--light{font-weight:400}
.h-side--light b{font-weight:700}
.why{left:32px;top:346px;width:158px}
.why__row{display:flex;align-items:center;gap:7px;height:26.5px;border-bottom:1px solid #cfcfcf;font-size:6.8px;font-weight:600;line-height:8px}
.why__row:last-child{border-bottom:none}
.why .icon{width:24px;height:24px;border:2px solid var(--navy);background:var(--yellow)}
.seal-rect{left:34px;top:488px;width:42px;height:54px;background:#fff;border:1.5px solid #27599a;border-radius:3px}
.seal-circle{left:92px;top:484px;width:60px;height:60px;border-radius:50%;background:#1f5fae;border:4px solid #c9ced6}
.rev-head{left:198px;top:266px;font-size:12px;font-weight:700;white-space:nowrap}
.rev-head__platform{color:var(--link-blue)}
.rev-head__stars{color:var(--yellow);letter-spacing:-1px}
.quote{left:198px;width:275px;height:16px;display:flex;justify-content:center}
.quote svg{width:20px;height:16px}
.review{left:198px;width:275px;background:var(--grey-box);border-radius:10px;padding:14px 14px 0;text-align:center;font-size:6.6px;line-height:8px;color:#333}
.review b{display:block;margin-top:7px;color:var(--ink);font-weight:600}
</style>
</head>
<body>

<!-- FRONT -->
<section class="page page--front">
  <div class="abs side-band"><div class="abs side-band__word">BLUE HERON</div></div>

  <div class="abs brand">
    <div class="brand__mark"></div>
    <div><div class="brand__name">BLUE HERON</div><div class="brand__tag">CONCRETE COATING</div></div>
  </div>

  <div class="abs bracket"></div>
  <div class="abs headline">
    <div class="headline__a">MAKING</div>
    <div class="headline__b">CONCRETE</div>
    <div class="headline__c">EXTRAORDINARY</div>
  </div>

  <div class="abs frame"></div>
  <div class="photo" role="img" aria-label="Speckled grey epoxy flake garage floor" style="left:52px;top:162px;width:168px;height:104px;background:linear-gradient(160deg,#b3b3b0,#8e8e8c)"></div>
  <div class="photo" role="img" aria-label="Close-up of swirled blue-grey metallic epoxy surface" style="left:52px;top:273px;width:168px;height:103px;background:linear-gradient(135deg,#3c4a60,#7b8aa1 50%,#2d3a50)"></div>
  <div class="photo" role="img" aria-label="Backyard pool deck with white spray texture coating and covered patio" style="left:226px;top:130px;width:232px;height:246px;background:linear-gradient(180deg,#7fa7d6 0%,#9bb4c8 22%,#6b6e60 35%,#dcdcd6 55%,#c9c9c2 80%,#6f7a55 100%)"></div>

  <div class="abs badge">
    <div class="badge__top">A PROUD<br>CERTIFIED<br>INSTALLER</div>
    <div class="badge__bot">OF STONECREST<br>PRODUCTS</div>
  </div>

  <div class="abs spec-title">WE <b>SPECIALIZE IN</b></div>
  <div class="abs spec-sub">Decorative concrete coatings; including</div>
  <ul class="abs list spec-col1">
    <li>Concrete staining and sealing</li>
    <li>Epoxy flake and quartz</li>
    <li>Polished Concrete</li>
    <li>Concrete resurfacing &amp; overlay</li>
  </ul>
  <ul class="abs list spec-col2">
    <li>Concrete crack repairs</li>
    <li>Pool deck spray texture</li>
    <li>Stamped concrete</li>
  </ul>

  <div class="abs about"><b>Our installation techniques</b> can transform your existing flooring, patio, countertops or pool deck to look like brick, marble, granite and so much more. Our decorative concrete surfaces will enhance the appearance of your home or business without the disruption and cost of exising surface removal.</div>

  <div class="abs owner-photo" role="img" aria-label="Portrait of the owner"></div>
  <div class="abs owner-name"><b>MARK</b> <span>ELLISON</span></div>
  <div class="abs owner-role">Owner</div>
  <div class="abs contacts">
    <div><svg viewBox="0 0 10 10"><circle cx="5" cy="5" r="5" fill="#f6c81b"/><path d="M3 2.6l1 .9-.5.8a3.5 3.5 0 0 0 2.2 2.2l.8-.5.9 1-.7.7C5 7.5 2.5 5 2.3 3.3z" fill="#1f2b3e"/></svg>404-555-0187</div>
    <div><svg viewBox="0 0 10 10"><circle cx="5" cy="5" r="5" fill="#f6c81b"/><rect x="2.4" y="3.2" width="5.2" height="3.6" fill="#1f2b3e"/><path d="M2.4 3.2L5 5.2l2.6-2" stroke="#f6c81b" stroke-width=".6" fill="none"/></svg>hello@blueheroncoating.com</div>
    <div><svg viewBox="0 0 10 10"><circle cx="5" cy="5" r="5" fill="#f6c81b"/><circle cx="5" cy="5" r="2.6" fill="none" stroke="#1f2b3e" stroke-width=".7"/><path d="M2.4 5h5.2M5 2.4v5.2" stroke="#1f2b3e" stroke-width=".6"/></svg>www.blueheroncoating.com</div>
  </div>
  <div class="abs free free--front free--dark"><div class="free__big">FREE</div><div class="free__small">ESTIMATES!</div></div>
</section>

<!-- BACK -->
<section class="page page--back">
  <div class="abs top-band"></div>
  <div class="abs svc-frame"></div>
  <div class="abs svc-title">OUR <b>SERVICE</b></div>
  <ul class="abs list list--light svc-list">
    <li>Decorative concrete coatings</li>
    <li>Concrete staining and sealing</li>
    <li>Epoxy flake and quartz</li>
    <li>Polished Concrete</li>
    <li>Concrete resurfacing &amp; overlay</li>
    <li>Concrete crack repairs</li>
    <li>Pool deck spray texture</li>
    <li>Stamped concrete</li>
  </ul>

  <div class="abs app-pill"><span>APPLICATIONS</span></div>
  <div class="abs app-frame"></div>
  <div class="abs app" style="left:246px;top:53px"><div class="icon"><svg viewBox="0 0 12 12"><path d="M1 5L6 1l5 4v6H1z" fill="none" stroke="#1f2b3e"/></svg></div>Garages</div>
  <div class="abs app" style="left:246px;top:79px"><div class="icon"><svg viewBox="0 0 12 12"><path d="M1 4h10M2 4v7M10 4v7M4 8h4" stroke="#1f2b3e" fill="none"/></svg></div>Patios</div>
  <div class="abs app" style="left:246px;top:104px"><div class="icon"><svg viewBox="0 0 12 12"><path d="M1 9q2.5-2 5 0t5 0M3 2v6M7 2v6" stroke="#1f2b3e" fill="none"/></svg></div>Pool decks</div>
  <div class="abs app" style="left:348px;top:53px"><div class="icon"><svg viewBox="0 0 12 12"><path d="M4 1L2 11M8 1l2 10M6 2v2M6 6v2" stroke="#1f2b3e" fill="none"/></svg></div>Driveways</div>
  <div class="abs app" style="left:348px;top:79px"><div class="icon"><svg viewBox="0 0 12 12"><rect x="1.5" y="1.5" width="9" height="9" fill="none" stroke="#1f2b3e"/><path d="M1.5 6h9" stroke="#1f2b3e"/></svg></div>Basements</div>
  <div class="abs app" style="left:348px;top:104px"><div class="icon"><svg viewBox="0 0 12 12"><path d="M1 4h10M2 4v7M10 4v7M5 1v3" stroke="#1f2b3e" fill="none"/></svg></div>Counter &amp; Bar tops</div>

  <div class="photo shot" role="img" aria-label="Grey resin quartz floor finish" style="left:32px;background:linear-gradient(160deg,#b8b8b8,#8a8a8a)"></div>
  <div class="photo shot" role="img" aria-label="Tan and brown epoxy flake floor" style="left:144px;background:linear-gradient(170deg,#d7cfc1 0%,#8e7d5e 45%,#6f6048)"></div>
  <div class="photo shot" role="img" aria-label="Grey stamped concrete walkway" style="left:256px;background:linear-gradient(170deg,#6c6e6a,#a9a9a4 55%,#7f807b)"></div>
  <div class="photo shot" role="img" aria-label="Spray textured cool deck beside a pool" style="left:368px;background:linear-gradient(160deg,#5f7f76,#c9ccc6 50%,#8a8d88)"></div>
  <div class="abs cap" style="left:32px">Resin Quartz</div>
  <div class="abs cap" style="left:144px">Epoxy Flake</div>
  <div class="abs cap" style="left:256px">Stamped Concrete</div>
  <div class="abs cap" style="left:368px">Spray Texture/Cool Deck</div>

  <div class="abs h-side" style="left:32px;top:268px">BENEFITS</div>
  <ul class="abs list" style="left:34px;top:286px;font-size:6.8px;line-height:10.6px">
    <li>Offer customers specialty upgrades</li>
    <li>Provide market differentiator</li>
    <li>Increase home market value</li>
  </ul>

  <div class="abs h-side h-side--light" style="left:32px;top:324px">WHY <b>US?</b></div>
  <div class="abs why">
    <div class="why__row"><div class="icon"></div>Proven residential and<br>commercial track record</div>
    <div class="why__row"><div class="icon"></div>Reliable &amp; quality workmanship</div>
    <div class="why__row"><div class="icon"></div>Best in industry products</div>
    <div class="why__row"><div class="icon"></div>Family owned and operated</div>
    <div class="why__row"><div class="icon"></div>Exclusive service provider for<br>Harlow &amp; Pinewood Homes</div>
  </div>
  <div class="abs seal-rect"></div>
  <div class="abs seal-circle"></div>

  <div class="abs rev-head" style="top:266px"><span class="rev-head__platform">KESTROVA</span> REVIEWS “<span class="rev-head__stars">★★★★★</span>” RATING</div>
  <div class="abs quote" style="top:280px"><svg viewBox="0 0 20 16"><path d="M1 9a5 5 0 0 1 6-7M11 9a5 5 0 0 1 6-7" stroke="#f6c81b" stroke-width="1.3" fill="none"/><circle cx="4.5" cy="11" r="3.5" fill="none" stroke="#f6c81b" stroke-width="1.3"/><circle cx="14.5" cy="11" r="3.5" fill="none" stroke="#f6c81b" stroke-width="1.3"/></svg></div>
  <div class="abs review" style="top:297px;height:58px;padding-top:12px">Mark's attention to detail is superb, he treats his jobs like he was doing his house! Highly recommend Mark at Blue Heron Coating, he is awesome, and his prices are very fair especially for the quality he delivers!<b>Laura Whitfield</b></div>
  <div class="abs quote" style="top:346px"><svg viewBox="0 0 20 16"><path d="M1 9a5 5 0 0 1 6-7M11 9a5 5 0 0 1 6-7" stroke="#f6c81b" stroke-width="1.3" fill="none"/><circle cx="4.5" cy="11" r="3.5" fill="none" stroke="#f6c81b" stroke-width="1.3"/><circle cx="14.5" cy="11" r="3.5" fill="none" stroke="#f6c81b" stroke-width="1.3"/></svg></div>
  <div class="abs review" style="top:362px;height:58px">Not only do they do amazing work, but the owner was on site every day, extremely responsive, timely, and professional. It's hard to find workmanship like that these days.<b>Nina Castell</b></div>

  <div class="abs rev-head" style="top:437px"><span class="rev-head__platform">QUILMORA</span> REVIEWS “<span class="rev-head__stars">★★★★★</span>” RATING</div>
  <div class="abs quote" style="top:452px"><svg viewBox="0 0 20 16"><path d="M1 9a5 5 0 0 1 6-7M11 9a5 5 0 0 1 6-7" stroke="#f6c81b" stroke-width="1.3" fill="none"/><circle cx="4.5" cy="11" r="3.5" fill="none" stroke="#f6c81b" stroke-width="1.3"/><circle cx="14.5" cy="11" r="3.5" fill="none" stroke="#f6c81b" stroke-width="1.3"/></svg></div>
  <div class="abs review" style="top:469px;height:75px">Mark was highly professional: he offered a competitive price, showed up when he told us he would, completed the job by the requested date, was flexible in working around my crazy work schedule, and was always clear in his communications. I would hire him again in a heartbeat and I recommend him highly<b>Peter Marsh</b></div>

  <div class="abs owner-photo" role="img" aria-label="Portrait of the owner"></div>
  <div class="abs owner-name"><b>MARK</b> <span>ELLISON</span></div>
  <div class="abs owner-role">Owner</div>
  <div class="abs contacts">
    <div><svg viewBox="0 0 10 10"><circle cx="5" cy="5" r="5" fill="#f6c81b"/><path d="M3 2.6l1 .9-.5.8a3.5 3.5 0 0 0 2.2 2.2l.8-.5.9 1-.7.7C5 7.5 2.5 5 2.3 3.3z" fill="#1f2b3e"/></svg>404-555-0187</div>
    <div><svg viewBox="0 0 10 10"><circle cx="5" cy="5" r="5" fill="#f6c81b"/><rect x="2.4" y="3.2" width="5.2" height="3.6" fill="#1f2b3e"/><path d="M2.4 3.2L5 5.2l2.6-2" stroke="#f6c81b" stroke-width=".6" fill="none"/></svg>hello@blueheroncoating.com</div>
    <div><svg viewBox="0 0 10 10"><circle cx="5" cy="5" r="5" fill="#f6c81b"/><circle cx="5" cy="5" r="2.6" fill="none" stroke="#1f2b3e" stroke-width=".7"/><path d="M2.4 5h5.2M5 2.4v5.2" stroke="#1f2b3e" stroke-width=".6"/></svg>www.blueheroncoating.com</div>
  </div>
  <div class="abs free free--back"><div class="free__big">FREE</div><div class="free__small">ESTIMATES!</div></div>
</section>

</body>
</html>
```